hostels chain website in Barcelona

We need a web design for a brand of youth hostels located in Barcelona called El Patio Mirasol. We have two hostels with different location. We offer cheap accomodation in shared dorms for young people (avg. 23 years old), but we aim to arrive to cultural tourist more than party people. We offer a local experience by hiring only local staff and by doing some free activities related to Barcelona.
Updates

Hello, In our website it has to appear the number and logo of the official agency that approve the bussiness. It is in our website, it is an orange box with the number 341 and 729. Besides this, we also like to have the wanderlogue box where it is possible to read reviews. Regards Marisol

Target Market(s)

Young people between 18 to 35 years old, that loves travelling and living new experiences.

Industry/Entity Type

Tourist

Other font styles liked:
• Gladifilthefte and Rockwell

Requirements
Must have
• Pictures of the hostel, booking buttom, groups section and activities section.
It must talk about two different locations.
Colors and design has to be related to the decoration of the hostel and the logo.
Nice to have
• It has to show happiness and cleanliness. we like the website http://www.patiolunahost.com/ as a reference.
Should not have
• Boring things

```html
<!DOCTYPE html>
<html lang="en">
<head>
<meta charset="utf-8">
<title>El Patio Mirasol Hostel</title>
<link rel="stylesheet" href="https://fonts.googleapis.com/css2?family=Arimo:wght@400&family=Squada+One&family=Six+Caps&display=swap">
<style>
  :root {
    --ink: #1f1f1f;
    --muted: #7a7a7a;
    --rule: #b5b5b5;
    --navy: #0f4470;
    --sky: #3a95d9;
    --red: #f03e33;
    --maroon: #a3120c;
    --gold: #ffc21a;
    --gold-ink: #7a5a0a;
    --gold-edge: #d9a010;
    --social: #3b5998;
    --display: "Squada One", "Arial Narrow", sans-serif;
    --tall: "Six Caps", "Arial Narrow", sans-serif;
    --body: "Arimo", Arial, sans-serif;
  }
  * { box-sizing: border-box; margin: 0; padding: 0; }
  html, body { width: 1200px; height: 904px; overflow: hidden; background: #fff; }
  body { position: relative; font-family: var(--body); color: var(--ink); }

  .brand { position: absolute; left: 100px; top: 26px; display: flex; align-items: flex-start; gap: 10px; }
  .brand-name { font-family: var(--display); font-size: 30px; line-height: 30px; color: var(--ink); width: 96px; }
  .brand-mark { width: 22px; height: 22px; margin-top: 16px; border-radius: 50%; background: var(--ink); }

  .social { position: absolute; left: 781px; top: 39px; display: flex; align-items: center; gap: 5px; font-size: 11px; }
  .social-square { width: 49px; height: 19px; background: var(--social); border-radius: 2px; }

  .languages { position: absolute; left: 780px; top: 77px; width: 340px; font-size: 9.5px; letter-spacing: 0.8px; color: var(--muted); line-height: 21px; white-space: nowrap; }
  .languages span { margin-right: 11px; }

  .main-nav { position: absolute; left: 101px; top: 133px; width: 998px; height: 33px;
    border-top: 1px dashed var(--rule); border-bottom: 1px dashed var(--rule);
    display: flex; justify-content: space-between; align-items: center; padding: 0 18px 0 3px; }
  .main-nav a { font-family: var(--display); font-size: 16px; font-style: italic; letter-spacing: 1.5px; color: var(--ink); text-decoration: none; }

  .hero { position: absolute; left: 100px; top: 185px; width: 1000px; height: 434px; border: 1px solid #bdbdbd; overflow: hidden; }
  .hero svg { display: block; }
  .hero-caption { position: absolute; left: 23px; top: 284px; font-family: var(--display); font-style: italic; font-size: 40px; line-height: 42px; letter-spacing: 3px; color: var(--ink); }

  .tiles { position: absolute; left: 101px; top: 636px; width: 999px; display: flex; justify-content: space-between; }
  .tile { width: 323px; height: 150px; display: flex; align-items: center; justify-content: center; font-family: var(--tall); font-size: 108px; line-height: 1; text-decoration: none; letter-spacing: 2px; }
  .tile-activities { background: var(--navy); color: var(--sky); }
  .tile-groups { background: var(--red); color: var(--maroon); letter-spacing: 12px; }
  .tile-book { background: var(--gold); color: var(--gold-ink); border: 1px solid var(--gold-edge); }

  .footer { position: absolute; left: 101px; top: 824px; width: 998px; border-top: 1px dashed var(--rule); padding-top: 13px; display: flex; font-size: 12.5px; }
  .footer nav { display: flex; }
  .footer nav a { color: var(--ink); text-decoration: none; margin-left: 3px; }
  .footer nav a + a { margin-left: 58px; }
  .footer .copyright { margin-left: auto; margin-right: 3px; }
</style>
</head>
<body>
  <header>
    <div class="brand">
      <span class="brand-name">El Patio Mirasol</span>
      <span class="brand-mark"></span>
    </div>
    <div class="social"><span class="social-square"></span><span>5,752 people like this.</span></div>
    <div class="languages">
      <span>ENGLISH</span><span>|</span><span>FRANÇAIS</span><span>|</span><span>PORTUGUÊS</span><span>|</span><span>BRASILEIRO</span><span>|</span><br>
      <span>ITALIANO</span><span>|</span><span>ESPAÑOL</span><span>|</span><span>NEDERLANDSE</span><span>|</span>
    </div>
    <nav class="main-nav">
      <a href="#">Home</a><a href="#">The Hostel</a><a href="#">Events</a><a href="#">Contact</a><a href="#">GALLERY</a><a href="#">FAQ'S</a>
    </nav>
  </header>

  <section class="hero">
    <svg width="1000" height="434" role="img" aria-label="Illustration of the hostel reception with staff at a wooden desk, teal and orange walls and up and down stairs doors">
      <defs>
        <linearGradient id="heroTone" x1="0" y1="0" x2="1" y2="0">
          <stop offset="0" stop-color="#ececec"/>
          <stop offset="0.3" stop-color="#e7c9bd"/>
          <stop offset="0.55" stop-color="#d9dcdc"/>
          <stop offset="0.72" stop-color="#8fb9bb"/>
          <stop offset="1" stop-color="#e3e3e3"/>
        </linearGradient>
      </defs>
      <rect width="1000" height="434" fill="url(#heroTone)"/>
    </svg>
    <p class="hero-caption">Sed ut perspiciatis<br>unde omnis iste natus .</p>
  </section>

  <section class="tiles">
    <a class="tile tile-activities" href="#">ACTIVITIES</a>
    <a class="tile tile-groups" href="#">GROUPS</a>
    <a class="tile tile-book" href="#">BOOK NOW !</a>
  </section>

  <footer class="footer">
    <nav><a href="#">Home</a><a href="#">The Hostel</a><a href="#">Events</a><a href="#">Contact</a><a href="#">GALLERY</a><a href="#">FAQ'S</a></nav>
    <span class="copyright">Copyright 2014</span>
  </footer>
</body>
</html>
```